Builder of high-end, expensive tables and other furniture

Build a website that represents what we do. I want a luxury feel that appeals to those who can afford our products. We build very high end tables and other furniture using trees that have fallen or are standing dead. We never cut living trees. Trees are harvested, milled, and kiln dried. Then that lumber is meticulously turned into fine furniture using the best equipment. Our furniture prices range from $1,000-$20,000.

Trying to figure out how to raise my spend.

```html
<!DOCTYPE html>
<html lang="en">
<head>
<meta charset="utf-8">
<title>Heirwood Tables</title>
<link href="https://fonts.googleapis.com/css2?family=Poppins:ital,wght@0,400;0,500;1,400;1,500;1,600&family=Lato:wght@400;700&family=Roboto:wght@400;500&display=swap" rel="stylesheet">
<style>
:root{
  --blue:#3a6fb5;
  --btn-blue:#2f6db5;
  --orange:#ef8420;
  --orange-light:#fbe3c8;
  --cart:#d9603b;
  --wood-dark:#6a3217;
  --wood-mid:#a4572a;
  --grey-bg:#f3f4f4;
  --line:#e4e4e4;
  --text:#222;
  --footer:#2b2f33;
}
*{margin:0;padding:0;box-sizing:border-box}
html,body{width:1200px;height:1200px;overflow:hidden;background:#fff}
.page{position:absolute;left:0;top:0;width:1920px;height:1920px;transform:scale(.625);transform-origin:0 0;font-family:'Poppins',sans-serif;color:var(--text)}
.abs{position:absolute}
.brand{font-family:'Poppins',sans-serif;font-weight:500;color:var(--orange);font-size:17px;display:flex;align-items:center;gap:6px;white-space:nowrap}
.brand .dot{width:10px;height:10px;border-radius:50%;background:var(--orange)}
.nav a{position:absolute;top:42px;font-size:13px;color:var(--blue);text-decoration:none}
.hero{left:486px;top:110px;width:908px;height:282px;background:radial-gradient(ellipse at 50% 40%,var(--wood-mid),var(--wood-dark) 85%);text-align:center;color:#fff}
.hero h1{font-style:italic;font-weight:500;font-size:22px;margin-top:46px}
.hero p{font-style:italic;font-size:12px;line-height:18px;width:780px;margin:4px auto 0}
.hero .explore{display:block;margin:30px auto 0;width:185px;height:17px;border-radius:9px;background:#f2a51a;border:1px solid #fff3;color:#fff;font-size:10px;line-height:16px}
.band{left:486px;width:900px;height:22px;background:linear-gradient(90deg,var(--orange),#f6b678 55%,var(--orange-light))}
.section-title{left:486px;width:908px;text-align:center;font-style:italic;font-weight:500;font-size:26px}
.rule{left:670px;width:540px;height:1px;background:var(--line)}
.filter{left:486px;top:508px;width:908px;height:36px;background:var(--grey-bg);font-family:'Roboto',sans-serif;font-size:12px}
.filter label{position:absolute;left:92px;top:16px}
.filter .select{position:absolute;left:194px;top:15px;width:102px;height:16px;border:1px solid #333;border-radius:2px;background:#fff;font-size:11px;padding-left:3px;line-height:14px}
.strip{left:524px;top:553px;width:829px;height:15px;background:var(--grey-bg)}
.photo{width:316px;height:219px;border-radius:6px;border:2px solid #fff;box-shadow:0 4px 10px #0004}
.card-title{width:316px;text-align:center;font-family:'Lato',sans-serif}
.card-title h3{font-size:16px;font-weight:700;color:#333}
.card-title span{font-size:12px;color:#555;display:block;margin-top:4px}
.qty{height:26px;width:58px;border:1px solid #ddd;display:flex;font-size:10px;color:#555}
.qty span{flex:1;text-align:center;line-height:24px}
.qty span+span{border-left:1px solid #ddd}
.cart{width:101px;height:27px;background:var(--cart);color:#fff;font-family:'Lato',sans-serif;font-weight:700;font-size:11px;text-align:center;line-height:27px}
.field-label{left:670px;font-style:italic;font-size:13px}
.input{left:670px;width:541px;height:27px;border:1px solid #ccc;border-radius:3px;font-size:12px;color:#777;padding:5px 9px}
.btn{background:var(--btn-blue);color:#fff;border-radius:3px;font-size:12px;text-align:center}
.login-zone{left:486px;top:1423px;width:908px;height:312px;background:var(--grey-bg)}
.login{left:736px;top:1440px;width:281px;height:244px;background:#fff;border:1px solid #ddd;border-radius:3px;font-family:'Roboto',sans-serif;padding:10px 9px}
.login h2{font-weight:400;font-size:20px}
.login label{display:block;font-size:11px;margin-top:24px;font-weight:400}
.login .box{height:27px;border:1px solid #ccc;border-radius:3px;font-size:11px;color:#666;padding:6px 9px;margin-top:3px}
.login .go{width:48px;height:27px;line-height:27px;margin-top:13px}
.login p{font-size:11px;margin-top:15px}
.login p a{color:var(--btn-blue);text-decoration:underline}
.footer{left:486px;top:1766px;width:908px;height:145px;background:var(--footer);color:#ccc;font-style:italic}
.footer .menu{position:absolute;left:379px;top:26px;font-size:9px;line-height:18px}
.footer .menu b{font-size:12px;font-weight:500;color:#fff;display:block}
.footer .info{position:absolute;left:240px;top:58px;font-size:9px;line-height:13px;color:#999}
.social{position:absolute;top:66px;width:8px;height:8px;border-radius:50%;background:#ccc}
</style>
</head>
<body>
<div class="page">
  <div class="abs brand" style="left:522px;top:40px"><span class="dot"></span>Heirwood Tables</div>
  <nav class="nav">
    <a style="left:738px">Our Story</a>
    <a style="left:830px">Products</a>
    <a style="left:920px">Contact Us</a>
    <a style="left:1023px">Log-in</a>
  </nav>

  <section class="abs hero" role="img" aria-label="Background photograph of warm wooden planks">
    <h1>Our Story</h1>
    <p>We build very tall tables and other furniture using trees that have fallen or are dead standing. We never cut living trees. Trees are harvested, milled, and kiln-dried. Then the wood is carefully turned into fine furniture using the best tools.</p>
    <span class="explore">Explore more</span>
  </section>
  <div class="abs band" style="top:391px"></div>

  <h2 class="abs section-title" style="top:458px">Products (Art Galery)</h2>
  <div class="abs rule" style="top:503px"></div>
  <div class="abs filter"><label>Select a category :</label><div class="select">Tables ⌄</div></div>
  <div class="abs strip"></div>

  <div class="abs photo" style="left:571px;top:570px;background:linear-gradient(150deg,#1b1a18,#3a2416 50%,#6b3d22 70%,#222)" role="img" aria-label="Teak coffee table with wine and cheese in a dark lounge"></div>
  <div class="abs card-title" style="left:571px;top:805px"><h3>Teak Table</h3><span>Price $ 2.000</span></div>
  <div class="abs qty" style="left:634px;top:870px"><span>-</span><span>1</span><span>+</span></div>
  <div class="abs cart" style="left:706px;top:869px">ADD TO CART</div>

  <div class="abs photo" style="left:993px;top:570px;background:linear-gradient(180deg,#e8eaec,#cfd2d4 55%,#4a3a30 80%,#8a8d8f)" role="img" aria-label="Bright kitchen with island table and pendant lamps"></div>
  <div class="abs card-title" style="left:993px;top:805px"><h3>Teak Table</h3><span>Price $ 1.500</span></div>
  <div class="abs qty" style="left:1061px;top:870px"><span>-</span><span>1</span><span>+</span></div>
  <div class="abs cart" style="left:1133px;top:869px">ADD TO CART</div>

  <div class="abs band" style="top:944px"></div>
  <h2 class="abs section-title" style="top:962px">Contact</h2>
  <div class="abs rule" style="top:1007px"></div>
  <div class="abs field-label" style="top:1020px">Name :</div>
  <div class="abs input" style="top:1044px">name</div>
  <div class="abs field-label" style="top:1084px">E-mail :</div>
  <div class="abs input" style="top:1107px">email</div>
  <div class="abs field-label" style="top:1148px">Phone :</div>
  <div class="abs input" style="top:1171px">Phone</div>
  <div class="abs field-label" style="top:1212px">Message :</div>
  <div class="abs input" style="top:1235px;height:64px"></div>
  <div class="abs btn" style="left:670px;top:1310px;width:49px;height:28px;line-height:28px">Send</div>

  <div class="abs band" style="top:1372px"></div>
  <div class="abs login-zone"></div>
  <div class="abs login">
    <h2>Login</h2>
    <label>Name:</label><div class="box">name</div>
    <label style="margin-top:18px">Password:</label><div class="box">Password</div>
    <div class="btn go">Login</div>
    <p>don't have account <a>Register</a></p>
  </div>

  <div class="abs band" style="top:1741px"></div>
  <footer class="abs footer">
    <div class="brand" style="position:absolute;left:216px;top:34px;font-style:normal;font-size:15px;font-weight:400"><span class="dot" style="width:7px;height:7px"></span>Heirwood Tables</div>
    <div class="info">Detail<br>Address<br><br>Phone</div>
    <div class="menu"><b>Menu</b>Our Story<br>Products<br>Conact Us<br>Log-in</div>
    <span class="social" style="left:556px"></span>
    <span class="social" style="left:573px"></span>
    <span class="social" style="left:590px"></span>
  </footer>
</div>
</body>
</html>
```